Chiropractic healthcare group business card

We are a Ashby Oregon based chiropractic healthcare group. Looking for a new business card design. Something cutting edge, that shows off our new logo and tag line.Use either of the attached logos.Our tag line = "Who would you be without pain?"I'm open to about anything, impress me!!
Target Market(s)
Chiropractic patients - Auto injury, back pain, sports injuries, neck , shoulder, hip, knee, ankle pain.
Industry/Entity Type
Chiropractic
Contact Information for Business Card
Dr. Bram Holtvick, D.C.
Clinic name - Fernway Chiropractic
2 clinics
location #1
20418 NW Marwick Road
Suite B
Marlow Plains, OR 97481
Location #2
13529 SE Calloway Street
Ashby OR 97592
Main phone line 971.555.0143
website : www.FernwayClinics.example
Tag line "Who would you be without pain?"
Colors
Designer to choose colors to be used in the design.
Requirements
Must have
- Use the logo colors -- Want the orange color to be a TRUE orange.
- Both clinic address
- phone number
- website
- personal email - b.holtvick@ReliefBeginsHere.example
- tag line - "Who would you be without pain?"

```html
<!DOCTYPE html>
<html lang="en">
<head>
<meta charset="utf-8">
<title>Fernway Chiropractic – Business Card</title>
<link rel="stylesheet" href="https://fonts.googleapis.com/css2?family=Montserrat:wght@400;500;600;700&family=Yellowtail&display=swap">
<style>
  :root {
    --true-orange: #ff7518;
    --orange-light: rgba(255, 255, 255, 0.09);
    --ink: #2b2b2b;
    --slate: #6b6b6b;
    --paper: #ffffff;
    --stage: #3c3c3c;
    --edge: #8a8a8a;
  }
  * { box-sizing: border-box; margin: 0; padding: 0; }
  html, body {
    width: 1200px; height: 900px; overflow: hidden;
    background: var(--stage);
    font-family: "Montserrat", sans-serif;
  }
  .canvas { position: relative; width: 1200px; height: 900px; }

  .card {
    position: absolute;
    width: 525px; height: 300px;
    border-radius: 3px;
    overflow: hidden;
    box-shadow: 0 14px 30px rgba(0,0,0,0.45);
  }

  /* Front */
  .card--front { left: 60px; top: 150px; background: var(--true-orange); }
  .front-band {
    position: absolute;
    background: var(--orange-light);
  }
  .front-band--upper { top: 172px; height: 26px; left: 110px; width: 310px; }
  .front-band--lower { top: 232px; height: 28px; left: 140px; width: 310px; }
  .front-brand {
    position: absolute; top: 78px; left: 0; width: 100%;
    text-align: center;
    color: var(--paper);
  }
  .front-brand-name {
    display: block;
    font-weight: 700; font-size: 32px; letter-spacing: 10px;
  }
  .front-brand-dot {
    display: inline-block; width: 12px; height: 12px;
    border-radius: 50%; background: var(--paper);
    margin-right: 12px; vertical-align: 5px;
  }
  .front-brand-sub {
    display: block; margin-top: 4px;
    font-weight: 400; font-size: 12px; letter-spacing: 4px;
  }
  .front-tagline {
    position: absolute; top: 190px; left: 0; width: 100%;
    text-align: center;
    font-family: "Yellowtail", cursive;
    font-size: 30px; color: var(--paper);
  }

  /* Back */
  .card--back {
    left: 615px; top: 450px; background: var(--paper);
    border-bottom: 6px solid var(--edge);
  }
  .back-brand {
    position: absolute; left: 34px; top: 86px; width: 230px;
    color: var(--slate);
  }
  .back-brand-dot {
    display: block; width: 14px; height: 14px; border-radius: 50%;
    background: var(--true-orange); margin-bottom: 10px;
  }
  .back-brand-name {
    display: block;
    font-weight: 700; font-size: 26px; letter-spacing: 6px; line-height: 1.1;
  }
  .back-brand-sub {
    display: block; margin-top: 4px;
    font-weight: 400; font-size: 11px; letter-spacing: 3.5px;
  }
  .back-contact { position: absolute; left: 276px; top: 56px; right: 16px; }
  .back-name { font-weight: 700; font-size: 17px; color: var(--ink); }
  .back-clinic {
    font-weight: 500; font-size: 11px; letter-spacing: 1.5px;
    color: var(--slate); margin: 3px 0 14px;
  }
  .contact-list { list-style: none; }
  .contact-item {
    display: flex; align-items: center; gap: 8px;
    font-size: 10.5px; color: var(--ink); margin-bottom: 6px;
    white-space: nowrap;
  }
  .contact-item svg { width: 12px; height: 12px; flex: none; fill: var(--true-orange); }
  .contact-accent { color: var(--true-orange); }

  .back-addresses {
    position: absolute; left: 34px; bottom: 22px;
    font-size: 10.5px; color: var(--slate); line-height: 1.7;
    font-style: normal;
  }
  .address-label { color: var(--true-orange); font-weight: 500; }
</style>
</head>
<body>
<main class="canvas">

  <section class="card card--front">
    <div class="front-band front-band--upper"></div>
    <div class="front-band front-band--lower"></div>
    <div class="front-brand">
      <span class="front-brand-name"><span class="front-brand-dot"></span>FERNWAY</span>
      <span class="front-brand-sub">CHIROPRACTIC</span>
    </div>
    <p class="front-tagline">Who would you be without pain?</p>
  </section>

  <section class="card card--back">
    <div class="back-brand">
      <span class="back-brand-dot"></span>
      <span class="back-brand-name">FERNWAY</span>
      <span class="back-brand-sub">CHIROPRACTIC</span>
    </div>

    <div class="back-contact">
      <h1 class="back-name">Dr. Bram Holtvick, D.C.</h1>
      <p class="back-clinic">Fernway Chiropractic</p>
      <ul class="contact-list">
        <li class="contact-item">
          <svg viewBox="0 0 24 24" aria-hidden="true"><path d="M6.6 10.8a15 15 0 006.6 6.6l2.2-2.2a1 1 0 011-.25 11.4 11.4 0 003.6.57 1 1 0 011 1V20a1 1 0 01-1 1A17 17 0 013 4a1 1 0 011-1h3.5a1 1 0 011 1c0 1.25.2 2.45.57 3.57a1 1 0 01-.25 1z"/></svg>
          971.555.0143
        </li>
        <li class="contact-item">
          <svg viewBox="0 0 24 24" aria-hidden="true"><path d="M7 1h10a2 2 0 012 2v18a2 2 0 01-2 2H7a2 2 0 01-2-2V3a2 2 0 012-2zm0 3v14h10V4zm5 15.5a1.2 1.2 0 100 2.4 1.2 1.2 0 000-2.4z"/></svg>
          971.555.0178
        </li>
        <li class="contact-item">
          <svg viewBox="0 0 24 24" aria-hidden="true"><path d="M2 5h20v14H2zm2 2v.5l8 5 8-5V7zm0 2.8V17h16V9.8l-8 5z"/></svg>
          <span>b.holtvick@<span class="contact-accent">ReliefBeginsHere</span>.example</span>
        </li>
        <li class="contact-item">
          <svg viewBox="0 0 24 24" aria-hidden="true"><path d="M12 2a10 10 0 100 20 10 10 0 000-20zm6.9 9h-3a15 15 0 00-1.3-6 8 8 0 014.3 6zM12 4c.9 1.2 1.8 3.6 1.9 7h-3.8c.1-3.4 1-5.8 1.9-7zM9.4 5a15 15 0 00-1.3 6h-3a8 8 0 014.3-6zM5.1 13h3a15 15 0 001.3 6 8 8 0 01-4.3-6zM12 20c-.9-1.2-1.8-3.6-1.9-7h3.8c-.1 3.4-1 5.8-1.9 7zm2.6-1a15 15 0 001.3-6h3a8 8 0 01-4.3 6z"/></svg>
          www.FernwayClinics.example
        </li>
      </ul>
    </div>

    <address class="back-addresses">
      <div><span class="address-label">Marlow Plains :</span> 20418 NW Marwick Rd, Suite B, Marlow Plains, OR 97481</div>
      <div><span class="address-label">Ashby Office :</span> 13529 SE Calloway St., Ashby, OR 97592</div>
    </address>
  </section>

</main>
</body>
</html>
```